New business card design

I need original, modern, business looking but dzen (minimalistic) looking design.
Also refer to websit trevanix.ru

Text is

Дробышев Кирилл, PMP
Партнер

Моб. +7 (915) 460 7185
info@trevanix.ru
Москва, Россия, 117342, ул. Береговая 7/2
=====================

Drobyshev Kirill, PMP
Partner

Mob. +7 (915) 460 7185
info@trevanix.ru
Moscow, Russia,117342, Beregovaya 7/2

Industry/Entity Type

Business

Font styles to use
Serif
Sans Serif

```html
<!DOCTYPE html>
<html lang="ru">
<head>
<meta charset="utf-8">
<title>Trevanix — визитная карточка</title>
<link rel="stylesheet" href="https://fonts.googleapis.com/css2?family=Arimo:ital,wght@0,400;1,400;1,700&display=swap">
<style>
  :root {
    --page-bg: #e9e7e4;
    --card-bg: #f6f6f6;
    --card-shade: #e4e4e4;
    --brand-blue: #2a86c9;
    --band-grey: #3d3f42;
    --ink-dark: #3a3b3d;
    --ink-soft: #2f3033;
  }
  * { box-sizing: border-box; margin: 0; padding: 0; }
  html, body {
    width: 1200px; height: 900px; overflow: hidden;
    background: var(--page-bg);
    font-family: "Arimo", Arial, sans-serif;
  }
  .canvas { position: relative; width: 1200px; height: 900px; }

  .card {
    position: absolute;
    width: 600px; height: 343px;
    border-radius: 26px;
    background: radial-gradient(circle at 55% 40%, #ffffff 0%, var(--card-bg) 55%, var(--card-shade) 100%);
    box-shadow: 0 10px 26px rgba(0,0,0,0.18);
    overflow: hidden;
  }
  .card--front { left: 90px; top: 90px; }
  .card--back  { left: 510px; top: 467px; }

  /* brand lockup */
  .brand { display: flex; align-items: center; gap: 22px; }
  .brand__mark { width: 58px; height: 58px; background: var(--brand-blue); border-radius: 8px; }
  .brand__name { font-size: 60px; font-weight: 400; color: var(--ink-dark); letter-spacing: -0.5px; line-height: 1; }

  .card--front .brand {
    position: absolute; inset: 0;
    justify-content: center;
  }

  /* back side */
  .card__band { position: absolute; left: 0; top: 0; width: 140px; height: 343px; }

  .contact { position: absolute; left: 150px; top: 78px; font-style: italic; }
  .contact__name { font-size: 24px; font-weight: 700; color: var(--brand-blue); line-height: 1.15; }
  .contact__role { font-size: 19px; color: var(--ink-soft); margin-top: 6px; }
  .contact__list { list-style: none; margin-top: 30px; }
  .contact__item {
    display: flex; align-items: flex-start; gap: 10px;
    font-size: 15px; line-height: 23px; color: var(--ink-soft);
  }
  .contact__icon { width: 15px; height: 15px; flex: none; margin-top: 4px; }

  .card--back .brand {
    position: absolute; right: 24px; bottom: 42px;
    flex-direction: column; align-items: center; gap: 22px;
  }
  .card--back .brand__mark { width: 90px; height: 90px; border-radius: 12px; }
  .card--back .brand__name { font-size: 46px; }
</style>
</head>
<body>
<main class="canvas">

  <section class="card card--front" aria-label="Лицевая сторона">
    <div class="brand">
      <span class="brand__mark"></span>
      <span class="brand__name">Trevanix</span>
    </div>
  </section>

  <section class="card card--back" aria-label="Оборотная сторона">
    <svg class="card__band" viewBox="0 0 140 343" aria-hidden="true">
      <path d="M0 0 H118 C78 70 62 170 78 343 H0 Z" fill="var(--band-grey)"/>
      <path d="M0 0 H100 C62 70 48 170 66 343 H0 Z" fill="var(--brand-blue)"/>
    </svg>

    <div class="contact">
      <p class="contact__name">Дробышев Кирилл, PMP</p>
      <p class="contact__role">Партнер</p>
      <ul class="contact__list">
        <li class="contact__item">
          <svg class="contact__icon" viewBox="0 0 16 16" aria-hidden="true"><rect x="4" y="1" width="8" height="14" rx="1.5" fill="none" stroke="var(--brand-blue)" stroke-width="1.6"/><circle cx="8" cy="12.3" r="0.9" fill="var(--brand-blue)"/></svg>
          <span>Моб. +7 (915) 460 7185</span>
        </li>
        <li class="contact__item">
          <svg class="contact__icon" viewBox="0 0 16 16" aria-hidden="true"><rect x="1" y="3.5" width="14" height="9" rx="1" fill="var(--brand-blue)"/><path d="M1.5 4 L8 9 L14.5 4" fill="none" stroke="#fff" stroke-width="1.2"/></svg>
          <span>info@trevanix.ru</span>
        </li>
        <li class="contact__item">
          <svg class="contact__icon" viewBox="0 0 16 16" aria-hidden="true"><g fill="none" stroke="var(--brand-blue)" stroke-width="1.3"><circle cx="8" cy="8" r="6.5"/><ellipse cx="8" cy="8" rx="3" ry="6.5"/><path d="M1.5 8 H14.5 M2.6 4.8 H13.4 M2.6 11.2 H13.4"/></g></svg>
          <span>www.trevanix.ru</span>
        </li>
        <li class="contact__item">
          <svg class="contact__icon" viewBox="0 0 16 16" aria-hidden="true"><path d="M8 15 C4 10 3 8 3 6 A5 5 0 0 1 13 6 C13 8 12 10 8 15 Z" fill="var(--brand-blue)"/><circle cx="8" cy="6" r="1.8" fill="#fff"/></svg>
          <span>Москва, Россия,<br>117342, ул. Береговая 7/2</span>
        </li>
      </ul>
    </div>

    <div class="brand">
      <span class="brand__mark"></span>
      <span class="brand__name">Trevanix</span>
    </div>
  </section>

</main>
</body>
</html>
```